A Label for an ECO Friendly Spirit Company

Design a label which can be used for vodka and gin (London Dry Gin). It should be Square type Like the Shape File you see in the uploads. VORK means Local Eco friendly Authentic and Fair. We want a cool and slim label that calls for eco-friendly. We want to use it for our premium
Vodka and our London Dry Gin. Please use the logo and design it in Square Type.

40%vol, 700ml

Target Market(s)

spirits and events

Industry/Entity Type

SPIRITS

Colors
00AB8E
00BBA5
67D7C9
C6EFE9
E9F9F6
59FF00
82FF00
B8FF75
E3FFCB
F4FFEA

Requirements
Must have
• Logo from VORK, Squaee Shape

```html
<!DOCTYPE html>
<html lang="en">
<head>
<meta charset="utf-8">
<title>VORK Vodka &amp; Gin Label</title>
<link rel="stylesheet" href="https://fonts.googleapis.com/css2?family=Metamorphous&family=Montserrat:wght@500&family=Tinos&display=swap">
<style>
  :root {
    --bg: #eef3f6;
    --label: #f7f9fa;
    --brand: #00bba5;
    --brand-mark: #67d7c9;
    --ink: #2b2b2b;
    --band: #9ee35c;
    --band-ink: #2f3a24;
    --small-ink: #333333;
  }
  html, body {
    margin: 0;
    padding: 0;
    width: 1200px;
    height: 1200px;
    overflow: hidden;
    background: var(--bg);
  }
  .label {
    position: relative;
    width: 1200px;
    height: 1200px;
    background: var(--label);
    box-sizing: border-box;
  }
  .brand {
    position: absolute;
    top: 250px;
    left: 0;
    right: 0;
    display: flex;
    align-items: center;
    justify-content: center;
    gap: 22px;
  }
  .brand-square {
    width: 70px;
    height: 70px;
    background: var(--brand-mark);
    border-radius: 10px;
  }
  .brand-name {
    font-family: "Montserrat", sans-serif;
    font-weight: 500;
    font-size: 96px;
    letter-spacing: 4px;
    line-height: 1;
    color: var(--brand);
  }
  .product-name {
    position: absolute;
    top: 480px;
    left: 0;
    right: 0;
    margin: 0;
    text-align: center;
    font-family: "Metamorphous", serif;
    font-weight: 400;
    font-size: 150px;
    line-height: 1.05;
    letter-spacing: 6px;
    color: var(--ink);
  }
  .variety-band {
    position: absolute;
    top: 820px;
    left: 330px;
    width: 540px;
    height: 78px;
    background: var(--band);
    display: flex;
    align-items: center;
    justify-content: center;
    font-family: "Tinos", serif;
    font-size: 48px;
    color: var(--band-ink);
  }
  .spec {
    position: absolute;
    top: 990px;
    font-family: "Tinos", serif;
    font-size: 34px;
    color: var(--small-ink);
  }
  .spec-abv { left: 150px; }
  .spec-volume { right: 150px; }
</style>
</head>
<body>
  <main class="label">
    <div class="brand">
      <span class="brand-square"></span>
      <span class="brand-name">VORK</span>
    </div>
    <h1 class="product-name">VODKA<br>&amp; GIN</h1>
    <div class="variety-band">London Dry Gin</div>
    <span class="spec spec-abv">40%vol</span>
    <span class="spec spec-volume">700ml</span>
  </main>
</body>
</html>
```